Harbormile Trade Associates - Letterhead and Folder

I am looking for letterhead that uses the splash from the logo on the side of the page as well as some information from our website.

I am looking for a folder that is a fold out that has pockets to hold paper as well as a slits for a business card.

Website address is www.harbormiletradeassociates.example

Target Market(s)

Export of Agrifoods, commodities and emergency aid.
Supplying the world food security.

Requirements
Must have
• Use splash and logo, have information about company.
• Letterhead must have splash on a side not in the middle.
Nice to have
• Different pictures that what are provided.

```html
<!DOCTYPE html>
<html lang="en">
<head>
<meta charset="utf-8">
<title>Harbormile Trade Associates – Letterhead and Folder</title>
<link href="https://fonts.googleapis.com/css2?family=Cinzel:wght@600&family=Arimo:wght@400;700&family=Yellowtail&display=swap" rel="stylesheet">
<style>
  :root {
    --backdrop: #b9b9bb;
    --paper: #ffffff;
    --ink: #1f1f1f;
    --teal: #0e8793;
    --leaf: #3d9b3f;
    --canola: #cfd13e;
    --meadow: #8fa83a;
    --bloom: #b9b844;
    --foliage: #3a5224;
  }
  * { margin: 0; padding: 0; box-sizing: border-box; }
  html, body { width: 1189px; height: 1200px; overflow: hidden; background: var(--backdrop); }
  .canvas { position: relative; width: 1189px; height: 1200px; }
  .sheet { position: absolute; top: 260px; background: var(--paper); overflow: hidden; font-family: "Arimo", Arial, sans-serif; color: var(--ink); }
  .letterhead { left: 34px; width: 527px; height: 680px; }
  .folder { left: 635px; width: 524px; height: 678px; }
  .sheet > svg { position: absolute; left: 0; top: 0; }
  .brand { position: absolute; display: flex; align-items: center; gap: 14px; }
  .brand-dot { border: 3px solid var(--leaf); border-radius: 50%; flex: none; }
  .brand-name { font-family: "Cinzel", Georgia, serif; font-weight: 600; color: var(--ink); line-height: 1.15; letter-spacing: 0.5px; }
  .letterhead .brand { left: 39px; top: 109px; }
  .letterhead .brand-dot { width: 68px; height: 68px; }
  .letterhead .brand-name { font-size: 17px; }
  .folder .brand { left: 259px; top: 30px; }
  .folder .brand-dot { width: 62px; height: 62px; }
  .folder .brand-name { font-size: 15px; }
  .contacts { position: absolute; left: 40px; top: 222px; list-style: none; font-size: 8.6px; line-height: 9.5px; }
  .contacts li { display: flex; align-items: center; gap: 4px; }
  .contacts svg { width: 7px; height: 7px; }
  .recipient { position: absolute; left: 40px; top: 280px; font-size: 8.6px; line-height: 10.5px; }
  .recipient strong { display: block; font-weight: 400; font-size: 10.5px; margin-bottom: 6px; }
  .body-copy { position: absolute; left: 40px; top: 346px; width: 446px; font-size: 9.4px; line-height: 15.5px; letter-spacing: -0.15px; }
  .body-copy p + p { margin-top: 15px; }
  .regards { position: absolute; left: 40px; top: 498px; font-size: 9.4px; }
  .signature { position: absolute; left: 40px; top: 520px; font-family: "Yellowtail", cursive; font-size: 33px; line-height: 40px; }
  .signatory { position: absolute; left: 40px; top: 568px; font-size: 9.6px; font-weight: 700; line-height: 11.5px; letter-spacing: 0.3px; }
  .footer-address { position: absolute; left: 40px; top: 660px; font-size: 8.6px; color: var(--paper); }
  .folder-web { position: absolute; left: 38px; top: 651px; font-size: 8.8px; }
</style>
</head>
<body>
<main class="canvas">

  <section class="sheet letterhead">
    <svg width="527" height="680" viewBox="0 0 527 680">
      <defs>
        <linearGradient id="fieldTone" x1="0" y1="0" x2="1" y2="1">
          <stop offset="0" stop-color="var(--canola)"/>
          <stop offset="1" stop-color="var(--meadow)"/>
        </linearGradient>
      </defs>
      <rect class="field-photo" role="img" aria-label="Photo of a blooming canola field under a blue sky" width="527" height="260" fill="url(#fieldTone)"/>
      <path d="M0,90 C120,82 360,78 440,106 C495,128 520,190 527,252 L527,680 L0,680 Z" fill="var(--paper)"/>
      <path class="footer-band" d="M0,614 C45,645 100,652 210,652 L430,648 C475,646 502,660 494,680 L0,680 Z" fill="var(--teal)"/>
    </svg>

    <div class="brand">
      <span class="brand-dot"></span>
      <div class="brand-name">HARBORMILE TRADE<br>ASSOCIATES</div>
    </div>

    <ul class="contacts">
      <li><svg viewBox="0 0 7 7"><rect width="7" height="7" fill="var(--teal)"/></svg>555 014 2290</li>
      <li><svg viewBox="0 0 7 7"><rect x="0.7" y="0.7" width="5.6" height="5.6" fill="none" stroke="var(--teal)" stroke-width="1.4"/></svg>hello@harbormiletrade.example</li>
      <li><svg viewBox="0 0 7 7"><circle cx="3.5" cy="3.5" r="3.5" fill="var(--teal)"/></svg>www.harbormiletradeassociates.example</li>
    </ul>

    <div class="recipient">
      <strong>ALEX MORGAN</strong>
      Street Name,City Name.<br>Zip Coad 0000
    </div>

    <div class="body-copy">
      <p>Lorem Ipsum is simply dummy text of the printing and typesetting industry. Lorem Ipsum has been the industry's standard dummy text ever since the 1500s, when an unknown printer took a galley of type and scrambled it to make a type specimen book. It has survived not only five centuries,but also the leap into a electronic typesetting, remaining essentially unchanged. It was popularised in the 1960s with the release of Letraset like Aldus PageMaker including versions of Lorem Ipsum.</p>
      <p>It is a long established fact that a reader will be distracted by the readable content of a page when looking at its layout, opposed to using 'Content here, content here', making it look like readable English. Many desktop and at its years, sometimes by accident, sometimes on purpose (injected humour and the like).</p>
    </div>

    <p class="regards">Regards,</p>
    <p class="signature">Jordan Vale</p>
    <p class="signatory">Jordan Vale<br>General Maneger</p>
    <p class="footer-address">418 Quayside Row, Port Alder, NS B3K 0A1</p>
  </section>

  <section class="sheet folder">
    <svg width="524" height="678" viewBox="0 0 524 678">
      <defs>
        <linearGradient id="bloomTone" x1="0" y1="0" x2="1" y2="1">
          <stop offset="0" stop-color="var(--foliage)"/>
          <stop offset="0.5" stop-color="var(--bloom)"/>
          <stop offset="1" stop-color="var(--foliage)"/>
        </linearGradient>
      </defs>
      <path class="bloom-photo" role="img" aria-label="Close-up photo of yellow canola blossoms" d="M0,110 C30,125 80,122 200,118 L330,116 C420,114 470,150 505,230 L524,270 L524,650 C500,632 470,630 420,632 L160,636 C90,640 60,640 40,600 C10,540 0,480 0,400 Z" fill="url(#bloomTone)"/>
    </svg>

    <div class="brand">
      <span class="brand-dot"></span>
      <div class="brand-name">HARBORMILE TRADE<br>ASSOCIATES</div>
    </div>

    <p class="folder-web">www.harbormiletradeassociates.example</p>
  </section>

</main>
</body>
</html>
```